Calderwell Homes

To produce a business card design for our newly established house building and development company, We have had a logo design done please see attached, our slogan is "Quality homes built with care"
Contact Information for Business Card
Adress on card needs to Read - 47 Hollowmere Lane, Ashbridge, Wendlemoorshire NN14 3QX. Director name Mark Ellery
Requirements
Must have
- Web adress is www.calderwell-homes.co.uk
- Email address is info@calderwell-homes.co.uk
- phone number 07700 900418

```html
<!DOCTYPE html>
<html lang="en">
<head>
<meta charset="utf-8">
<title>Calderwell Homes – Business Card</title>
<link rel="stylesheet" href="https://fonts.googleapis.com/css2?family=Roboto:wght@400;500;700&family=Roboto+Condensed:wght@700&display=swap">
<style>
  :root {
    --green: #8cc63e;
    --grey: #9b9b9b;
    --ink: #4a4a4a;
    --paper: #ffffff;
    --backdrop: #ececec;
  }
  * { margin: 0; padding: 0; box-sizing: border-box; }
  html, body { width: 1125px; height: 1200px; overflow: hidden; }
  body {
    background: var(--backdrop);
    font-family: "Roboto", Arial, sans-serif;
    position: relative;
  }
  .card {
    position: absolute;
    left: 150px;
    width: 826px;
    height: 472px;
    overflow: hidden;
    box-shadow: 0 3px 8px rgba(0,0,0,0.25);
  }
  .card--front { top: 106px; background: var(--paper); }
  .card--back { top: 638px; background: var(--green); }

  .brand {
    position: absolute;
    text-align: center;
  }
  .card--front .brand { left: 74px; top: 232px; width: 350px; }
  .brand__name {
    font-family: "Roboto", Arial, sans-serif;
    font-weight: 700;
    font-size: 31px;
    letter-spacing: 1px;
    line-height: 1;
    white-space: nowrap;
    color: var(--green);
  }
  .brand__tagline {
    margin-top: 14px;
    font-size: 8px;
    font-weight: 500;
    letter-spacing: 4.6px;
    white-space: nowrap;
    color: var(--green);
  }

  .contact { position: absolute; left: 446px; top: 116px; color: var(--ink); }
  .contact__name {
    font-family: "Roboto Condensed", Arial, sans-serif;
    font-weight: 700;
    font-size: 29px;
    color: var(--green);
    line-height: 1;
  }
  .contact__role {
    margin-top: 6px;
    padding-left: 3px;
    font-size: 19px;
    font-weight: 500;
    color: var(--grey);
  }
  .contact__address {
    margin-top: 18px;
    font-size: 19px;
    line-height: 26px;
  }
  .contact__list { list-style: none; margin-top: 12px; font-size: 19px; line-height: 26px; }
  .contact__list li { display: flex; align-items: center; gap: 12px; }
  .contact__list svg { width: 18px; height: 18px; fill: var(--green); flex: none; }

  .footer-rule {
    position: absolute; left: 0; right: 0; top: 418px;
    height: 4px; background: var(--grey);
  }
  .footer-band {
    position: absolute; left: 0; right: 0; bottom: 0; height: 44px;
    background: var(--green);
    display: flex; align-items: center;
    padding-left: 187px;
    color: var(--paper);
    font-size: 19px; letter-spacing: 3.5px;
  }

  .card--back .brand { left: 0; right: 0; top: 178px; }
  .card--back .brand__name { color: var(--paper); font-size: 40px; letter-spacing: 2px; }
  .card--back .brand__tagline { color: var(--paper); font-size: 9px; letter-spacing: 5.5px; margin-top: 22px; }
  .brand__mark {
    width: 26px; height: 26px; background: var(--paper);
    margin: 0 auto 26px;
  }
  .back-url {
    position: absolute; left: 0; right: 0; top: 405px;
    text-align: center;
    color: var(--paper);
    font-size: 19px; letter-spacing: 3.5px;
  }
</style>
</head>
<body>
  <section class="card card--front">
    <div class="brand">
      <div class="brand__name">CALDERWELL HOMES</div>
      <div class="brand__tagline">QUALITY HOMES BUILT WITH CARE</div>
    </div>

    <div class="contact">
      <div class="contact__name">MARK ELLERY</div>
      <div class="contact__role">DIRECTOR</div>
      <p class="contact__address">47 Hollowmere Lane, Ashbridge<br>Wendlemoorshire NN14 3QX.</p>
      <ul class="contact__list">
        <li>
          <svg viewBox="0 0 24 24" aria-hidden="true"><path d="M6.6 10.8a15.1 15.1 0 0 0 6.6 6.6l2.2-2.2c.3-.3.7-.4 1-.2 1.1.4 2.3.6 3.6.6.6 0 1 .4 1 1V20c0 .6-.4 1-1 1A17 17 0 0 1 3 4c0-.6.4-1 1-1h3.5c.6 0 1 .4 1 1 0 1.3.2 2.5.6 3.6.1.3 0 .7-.2 1z"/></svg>
          07700 900418
        </li>
        <li>
          <svg viewBox="0 0 24 24" aria-hidden="true"><path d="M2 5h20v2l-10 6L2 7z"/><path d="M2 9l10 6 10-6v10H2z"/></svg>
          info@calderwell-homes.co.uk
        </li>
      </ul>
    </div>

    <div class="footer-rule"></div>
    <div class="footer-band">WWW.CALDERWELL-HOMES.CO.UK</div>
  </section>

  <section class="card card--back">
    <div class="brand">
      <div class="brand__mark"></div>
      <div class="brand__name">CALDERWELL HOMES</div>
      <div class="brand__tagline">QUALITY HOMES BUILT WITH CARE</div>
    </div>
    <div class="back-url">WWW.CALDERWELL-HOMES.CO.UK</div>
  </section>
</body>
</html>
```